Designing a Chocolate Bar's Package

We are a chocolate manufacturing company located in Lebanon. We produce chocolate on a wholesale level, and we are planning a new line of production at the moment.
We intend to be make small chocolate bars (about 30g) similar to the "Varmo Radiance" bar with several flavors. 2 flavors have been decided so far (Mint flavored dark chocolate and Plain dark chocolate).
The packaging material will be similar to varmo's package as well. It won't be a carton box. It'll be some sort of paper wrapping the entire bar. So I am looking for a design that has a unique and cool front and back look.
If only one design is to be prepared, please choose either the mint's flavor or the plain dark chocolate, and prepare the design accordingly.
Updates
Project Deadline Extended
Reason: I still have some time to begin the production. The new deadline,therefore, is the end of this month.
Target Market(s)
basically all chocolate lovers...
Industry/Entity Type
It Company
Requirements
Must have
- I will be uploading our logo. Please make sure to use it in the design.

```html
<!DOCTYPE html>
<html lang="en">
<head>
<meta charset="utf-8">
<title>Corvella Chocolate Bar Wrappers</title>
<link rel="stylesheet" href="https://fonts.googleapis.com/css2?family=Barlow:wght@400;500&display=swap">
<style>
  :root {
    --backdrop: #e3e4e5;
    --mint-green: #8dbf3f;
    --plain-orange: #f15a22;
    --wrapper-white: #ffffff;
    --foil-gold-dark: #b8945a;
    --foil-gold-light: #f1dfb4;
    --cocoa-brown: #5b3520;
    --tagline-gold: #b08a4a;
    --ink-dark: #3a2a20;
    --label-white: #ffffff;
  }
  * { box-sizing: border-box; margin: 0; padding: 0; }
  html, body {
    width: 1162px;
    height: 1200px;
    overflow: hidden;
    background: var(--backdrop);
  }
  .canvas {
    position: relative;
    width: 1162px;
    height: 1200px;
    font-family: "Barlow", "Helvetica Neue", Arial, sans-serif;
  }
  .wrapper {
    position: absolute;
    top: 98px;
    width: 490px;
    height: 1010px;
    border-radius: 12px;
    overflow: hidden;
    box-shadow: 0 2px 6px rgba(0,0,0,0.12);
  }
  .wrapper--mint { left: 72px; background: var(--mint-green); }
  .wrapper--plain { left: 594px; background: var(--plain-orange); }

  .foil-seal {
    position: absolute;
    left: 0;
    width: 100%;
    height: 18px;
    background: linear-gradient(90deg, var(--foil-gold-dark), var(--foil-gold-light) 30%, var(--foil-gold-dark) 55%, var(--foil-gold-light) 80%, var(--foil-gold-dark));
  }
  .foil-seal--top { top: 0; }
  .foil-seal--bottom { bottom: 0; }

  .brand-band {
    position: absolute;
    top: 45px;
    left: 0;
    width: 100%;
    height: 342px;
    background: var(--wrapper-white);
    text-align: center;
  }
  .brand-name {
    position: absolute;
    top: 92px;
    left: 0;
    width: 100%;
    font-size: 86px;
    line-height: 90px;
    font-weight: 500;
    color: var(--cocoa-brown);
    letter-spacing: 1px;
  }
  .brand-tagline {
    position: absolute;
    top: 196px;
    left: 0;
    width: 100%;
    font-size: 36px;
    line-height: 40px;
    font-weight: 400;
    color: var(--tagline-gold);
    letter-spacing: 1px;
  }
  .brand-audience {
    position: absolute;
    top: 245px;
    left: 0;
    width: 100%;
    font-size: 20px;
    line-height: 24px;
    font-weight: 400;
    color: var(--ink-dark);
    letter-spacing: 0.5px;
  }

  .product-photo {
    position: absolute;
    top: 402px;
    left: 125px;
    width: 272px;
    height: 372px;
    border-radius: 6px;
    background: linear-gradient(160deg, #4a2c1f, #2a160e 60%, #3b2217);
  }
  .product-photo--mint {
    background:
      radial-gradient(ellipse 100px 75px at 200px 250px, #7fc24a 0%, #5aa23a 60%, transparent 62%),
      linear-gradient(160deg, #4a2c1f, #2a160e 60%, #3b2217);
  }

  .flavour-label {
    position: absolute;
    top: 806px;
    left: 0;
    width: 100%;
    text-align: center;
    color: var(--label-white);
  }
  .flavour-name,
  .flavour-type {
    font-size: 32px;
    line-height: 44px;
    font-weight: 400;
    letter-spacing: 0.5px;
  }
  .net-weight {
    margin-top: 18px;
    font-size: 30px;
    line-height: 40px;
    font-weight: 400;
  }
</style>
</head>
<body>
<main class="canvas">

  <section class="wrapper wrapper--mint">
    <div class="foil-seal foil-seal--top"></div>
    <header class="brand-band">
      <div class="brand-name">Corvella</div>
      <div class="brand-tagline">Quality Chocolate</div>
      <div class="brand-audience">FOR CHOCOLATE LOVERS</div>
    </header>
    <div class="product-photo product-photo--mint" role="img" aria-label="Photo of stacked dark chocolate squares with a sprig of fresh mint leaves"></div>
    <div class="flavour-label">
      <p class="flavour-name">Mint flavored</p>
      <p class="flavour-type">DARK CHOCOLATE</p>
      <p class="net-weight">30g</p>
    </div>
    <div class="foil-seal foil-seal--bottom"></div>
  </section>

  <section class="wrapper wrapper--plain">
    <div class="foil-seal foil-seal--top"></div>
    <header class="brand-band">
      <div class="brand-name">Corvella</div>
      <div class="brand-tagline">Quality Chocolate</div>
      <div class="brand-audience">FOR CHOCOLATE LOVERS</div>
    </header>
    <div class="product-photo" role="img" aria-label="Photo of stacked plain dark chocolate squares"></div>
    <div class="flavour-label">
      <p class="flavour-name">Plain</p>
      <p class="flavour-type">DARK CHOCOLATE</p>
      <p class="net-weight">30g</p>
    </div>
    <div class="foil-seal foil-seal--bottom"></div>
  </section>

</main>
</body>
</html>
```